Chinese citizens moving to SYDNEY!

We need an A5 size flier for our new business. We would like this to be a fold-out flyer (brochure-style, i.e. 4 sides - front cover, middle, back cover). Full colour print (or 4 colour if it can be done without compromising the look). We need two versions of the same flyer - one in Chinese and one in English. Same design and imagery, just different languages. Copy is attached with imagery (subject to change once we source high res images).

Target Market(s)

Chinese citizens looking to emigrate to Sydney AND Chinese citizens who have recently moved to Sydney.

Industry/Entity Type

Business

Font styles to use
Sans Serif

Colors
ec1f27
000000
ffffff
fece3e

Requirements
Must have
• The front cover of the flier must be clean looking and show just our business name and tag line, along with an image of Sydney Harbour (provided). Main information ideally to be spread across the 2 centre pages with the back page quite clean, but if the text is too small we could consider it being spread across the remaining 3 pages (i.e. centre of the brochure, then the back cover).
• We would like it to be a clean and easy to read design. Suggested colours are written in the brief.
• It would be ideal to have a designer who can read Mandarin so that they know which characters make up a headline, which characters should not be spaced over two rows of text etc.

```html
<!DOCTYPE html>
<html lang="zh-CN">
<head>
<meta charset="utf-8">
<title>悦居生活 · 服务介绍</title>
<link href="https://fonts.googleapis.com/css2?family=Noto+Serif+SC:wght@400;600;700&display=swap" rel="stylesheet">
<style>
  :root {
    --brand-red: #c4262e;
    --bullet-red: #d3262e;
    --ink: #2a2a2a;
    --white: #ffffff;
    --dark: #222429;
    --bg-light: #f4f4f5;
    --bg-mid: #dcdde0;
  }
  * { margin: 0; padding: 0; box-sizing: border-box; }
  html, body { width: 1200px; height: 848px; overflow: hidden; }
  body { font-family: "Noto Serif SC", serif; color: var(--ink); background: var(--white); }

  .spread { position: relative; width: 1200px; height: 848px; overflow: hidden; }

  .backdrop {
    position: absolute; inset: 0;
    background:
      linear-gradient(180deg, rgba(255,255,255,0.92) 0%, rgba(255,255,255,0.55) 45%, rgba(255,255,255,0.75) 100%),
      linear-gradient(120deg, var(--bg-light) 0%, var(--bg-mid) 40%, var(--bg-light) 60%, var(--bg-mid) 100%);
  }

  .intro {
    position: absolute; left: 18px; top: 20px; width: 561px; height: 341px;
    background: var(--brand-red); color: var(--white);
    padding: 26px 16px 0 22px;
    font-size: 21.5px; line-height: 30px; text-align: justify; letter-spacing: 0.5px;
  }

  .family-photo {
    position: absolute; left: 932px; top: -4px; width: 280px; height: 280px;
    border-radius: 50%;
    background: radial-gradient(circle at 40% 45%, #f3d2b8 0%, #cfe3f3 45%, #8fbde0 75%, #5f9cd0 100%);
    border: 4px solid rgba(255,255,255,0.9);
  }

  .services-lead {
    position: absolute; left: 32px; top: 424px;
    font-size: 24px; font-weight: 600; letter-spacing: 1px; color: #333;
  }

  .section { position: absolute; }
  .section-rule { position: absolute; height: 2px; background: var(--brand-red); }
  .section-tag {
    position: absolute; background: var(--brand-red); color: var(--white);
    font-weight: 700; font-size: 23px; letter-spacing: 2px;
    border-radius: 18px 6px 18px 6px; display: flex; align-items: center; justify-content: center;
  }

  .service-list { position: absolute; list-style: none; }
  .service-list li { position: relative; padding-left: 16px; white-space: nowrap; }
  .service-list li::before {
    content: ""; position: absolute; left: 1px; top: 50%; width: 6px; height: 6px;
    margin-top: -3px; border-radius: 50%; background: var(--bullet-red);
  }
  .service-list li.cont::before { display: none; }

  .list-home { left: 630px; top: 62px; font-size: 20.5px; line-height: 27px; }
  .list-daily { left: 630px; top: 366px; font-size: 18.5px; line-height: 24px; }
  .list-health { left: 630px; top: 654px; font-size: 18.5px; line-height: 24px; }
  .list-school { left: 30px; top: 569px; font-size: 20.5px; line-height: 25.7px; }

  .footer-band { position: absolute; left: 0; bottom: 0; width: 1200px; height: 20px; }
</style>
</head>
<body>
<main class="spread">
  <div class="backdrop" role="img" aria-label="淡灰色的悉尼海港大桥城市背景照片"></div>

  <section class="intro">
    <p>悦居生活向计划在澳洲移民及投资的家庭提供私人管家服务。建立在悉尼。悦居生活帮助新移民家庭更快融于澳洲生活。我们团队中的悉尼本土人士可以在生活上的各个方面提供帮助-解答问题，提供建议，消除语言障碍。我们向家庭提供私人定制服务以满足不同家庭的不同需求。无论是帮子女择校、了解哪里可以买菜、介绍高水平的医生，悦居生活都可以满足您的需求。我们会给您的家庭分配一个精通中英文的专业私人助理，让你的移民之路更加简单、快乐！</p>
  </section>

  <div class="family-photo" role="img" aria-label="海边一家三口欢笑的圆形照片"></div>

  <h2 class="services-lead">我们的服务包括但不仅限于以下内容：</h2>

  <!-- Housing & vehicles -->
  <div class="section-rule" style="left:622px; top:34px; width:336px;"></div>
  <div class="section-tag" style="left:622px; top:21px; width:160px; height:30px;">房屋及车辆</div>
  <ul class="service-list list-home">
    <li>推荐最好的购房区域</li>
    <li>介绍房屋中介、协助买房流程</li>
    <li>安排入户及家具整理服务</li>
    <li>安排购买家电</li>
    <li>安排最好的公共事业公司接入</li>
    <li class="cont">水电气、电话、网络、电视等等</li>
    <li>安排清洁工、园丁等等</li>
    <li>比较及安排购买保险</li>
    <li>安排买车、租车及相关保险</li>
  </ul>

  <!-- Daily life -->
  <div class="section-rule" style="left:622px; top:335px; width:516px;"></div>
  <div class="section-tag" style="left:622px; top:318px; width:102px; height:34px; font-size:25px;">日常</div>
  <ul class="service-list list-daily">
    <li>介绍本地可以买菜的地方比如超市、特殊店铺、亚洲超市等</li>
    <li>推荐美发沙龙、美甲、美容等服务</li>
    <li>介绍购物中心、奢侈品品牌</li>
    <li>介绍高质量水暖工、电工、油漆工等</li>
    <li>帮助注册驾照、医保等</li>
    <li>帮助银行开户、开通网上银行</li>
    <li>帮助注册图书馆、健身房、高尔夫俱乐部会员等会员</li>
    <li>介绍私人及公共交通</li>
    <li>安排私人以及团体语言课程</li>
    <li>翻译文件、信件</li>
  </ul>

  <!-- Health & lifestyle -->
  <div class="section-rule" style="left:600px; top:632px; width:548px;"></div>
  <div class="section-tag" style="left:632px; top:618px; width:204px; height:30px;">健康及生活方式</div>
  <ul class="service-list list-health">
    <li>比较家庭保险</li>
    <li>推荐医务人员-医生、牙医、针灸等</li>
    <li>推荐餐馆</li>
    <li>推荐周边的公园及户外活动</li>
    <li>介绍当地的危险比如澳洲野生动物、海滩安全等等</li>
    <li>介绍家庭郊游、度假目的地，安排儿童生日派对、儿童小聚等</li>
    <li>安排司机</li>
  </ul>

  <!-- Schools -->
  <div class="section-rule" style="left:0; top:516px; width:579px;"></div>
  <div class="section-tag" style="left:30px; top:502px; width:102px; height:32px; font-size:24px;">学校</div>
  <ul class="service-list list-school">
    <li>推荐最好的学校和幼儿园</li>
    <li>比较学校排名和学术水平</li>
    <li>安排参观学校以及拜访校长</li>
    <li>帮助提交申请直到录取</li>
    <li>协助开学之后买校服、书本、了解学校等事宜</li>
    <li>安排家教帮助学英语以及辅导作业</li>
    <li>安排钢琴、网球以及其他课外活动</li>
    <li>翻译所有学校信件比如成绩单、作业等等</li>
  </ul>

  <svg class="footer-band" viewBox="0 0 1200 20" preserveAspectRatio="none" aria-hidden="true">
    <polygon points="0,0 104,0 96,20 0,20" fill="var(--dark)"/>
    <polygon points="110,0 800,0 792,20 102,20" fill="var(--brand-red)"/>
    <polygon points="806,0 1200,0 1200,20 798,20" fill="var(--dark)"/>
  </svg>
</main>
</body>
</html>
```